The Corvel Dental centre, the Zorvik of dentistry

New concept of running a dental practice by having a walk in practice
WE ARE A HUSBAND AND WIFE TEAM

Really modern and sophisticated, we want it to feel different from the traditional dental practice.
we want it split into different pages:CONTACT US
LOCATION: Information about our location since patients often confuse us with the practice across the road
ABOUT US:
Opening hours - & 7 Days, We offer a weekend service
WALK IN: We offer a walk in service for dental treatments
TREATMENTS we offer

DENTAL ADVICE: Free dentist advise call back- So a dentist will call you back for free to discuss

Target Market(s)

Everyone

Industry/Entity Type

Dental

Coding

Coded - Design and coding required

Number of Pages Required

5+ page

Requirements
Must have
• First page
• * changing pictures
• *opening times
• * our walk in concept I.e. no appointment needed
• *logo
• * links in to medi portal (online booking system in Australia)
• * address /phone number/email
• * possible videos
• Second page
• meet the team
• third page
• dental treatments/walk in treatments
• fourth page
• dental advice with you tube videos
• Fifth page
• contact us/maps/ we get confused with the dental practice across the road
• We would also like a giving back page. In this please include the photo's below of our dental mission in Guatemala, where by we did treatment for patients as part of a charity.
Nice to have
• Changing pictures on the home screen
• videos linked to home page

```html
<!DOCTYPE html>
<html lang="en">
<head>
<meta charset="utf-8">
<title>The Corvel Dental Centre</title>
<link href="https://fonts.googleapis.com/css2?family=Raleway:wght@400;500;600&family=Open+Sans:wght@400;600&display=swap" rel="stylesheet">
<style>
:root{
  --blue:#1ba6e4;
  --blue-dark:#0a8fd3;
  --green:#6cbf3a;
  --green-dark:#4f9e22;
  --ink:#333;
  --muted:#8a8a8a;
  --line:#d8d8d8;
  --soft:#f3f3f3;
}
*{box-sizing:border-box;margin:0;padding:0}
html,body{width:683px;height:1200px;overflow:hidden;background:#fff}
body{position:relative;font-family:"Open Sans",sans-serif;color:var(--ink)}
.abs{position:absolute}
/* header */
.brand{left:66px;top:12px;display:flex;align-items:center;gap:7px}
.brand-mark{width:30px;height:30px;border-radius:50%;background:var(--green);flex:none}
.brand-name{font-family:"Raleway",sans-serif;font-weight:600;font-size:14px;color:var(--green);line-height:1.1;width:130px}
.hours{left:370px;top:26px;font-size:8.5px;color:#444;white-space:nowrap}
.hours span{display:block;color:var(--blue);font-size:7.5px;margin-top:3px}
.call{left:508px;top:21px;text-align:right;width:110px;white-space:nowrap}
.call small{display:block;font-size:8px;color:var(--green)}
.call b{font-weight:400;font-size:12px;color:#333;display:flex;align-items:center;gap:3px;justify-content:flex-end;margin-top:1px}
/* nav */
.nav{left:0;top:61px;width:683px;height:29px;background:linear-gradient(#2ab6f0,#0f99dc);display:flex;padding-left:66px}
.nav a{color:#fff;text-decoration:none;font-size:9.5px;padding:0 14px;line-height:29px;border-right:1px solid rgba(255,255,255,.35);white-space:nowrap}
.nav a.active{background:var(--blue-dark);padding:0 22px;border:0}
.nav a:last-child{border:0}
/* hero */
.hero{left:0;top:90px;width:683px;height:272px;background:linear-gradient(100deg,#bfb9b4 0%,#8f8580 35%,#5e5a5e 60%,#3d4350 100%)}
.hero-text{left:69px;top:214px;color:#fff;font-family:"Raleway",sans-serif;white-space:nowrap}
.hero-text p{font-size:15px;letter-spacing:.2px}
.hero-text h1{font-size:21px;font-weight:500;margin-top:4px}
.dots{left:322px;top:344px;display:flex;gap:3px}
.dots i{width:9px;height:9px;border-radius:50%;background:#fff;display:block}
.dots i.on{background:var(--green);border:1.5px solid #fff}
/* welcome */
.welcome{left:67px;top:394px;width:300px}
.welcome h2{font-family:"Raleway",sans-serif;font-weight:400;font-size:15px;color:#333;margin-bottom:12px;white-space:nowrap}
.welcome p{font-size:7.2px;color:#777;line-height:16.5px;white-space:nowrap}
.welcome p.note{line-height:10.5px;margin-top:6px;color:#999}
.welcome-actions{display:flex;align-items:center;gap:18px;margin-top:12px}
.btn-green{background:linear-gradient(#6fcb36,#4ea91f);color:#fff;font-size:7px;font-weight:600;padding:7px 12px;border-radius:2px;width:71px;text-align:center}
.partner{display:flex;align-items:center;gap:5px;font-family:"Raleway",sans-serif;font-size:14px;color:#1f4f6e}
.partner i{width:12px;height:12px;background:var(--blue);display:block}
.video{left:384px;top:388px;width:236px;height:150px;background:#222}
.video-frame{position:absolute;inset:0 0 19px 0;background:linear-gradient(160deg,#e9ebea 0%,#c7cbcb 50%,#8fb35c 80%,#b7bdbb 100%)}
.video svg.play{position:absolute;left:96px;top:48px}
.video-bar{position:absolute;left:6px;right:6px;bottom:6px;height:8px;display:flex;align-items:center;gap:6px}
.track{flex:1;height:4px;background:#999;border-radius:2px;position:relative}
.track i{position:absolute;left:0;top:0;height:4px;width:40%;background:var(--blue);border-radius:2px}
/* features */
.features{left:0;top:575px;width:683px;height:206px;background:linear-gradient(90deg,#e7e7e7,#f2f2f2 40%,#ececec);border-top:1px solid #e2e2e2;border-bottom:1px solid #e2e2e2}
.feature{position:absolute;top:27px;width:180px;text-align:center}
.feature-icon{width:75px;height:75px;border-radius:50%;margin:0 auto;border:3px solid #fff;outline:2px solid var(--green);display:flex;align-items:center;justify-content:center;background:var(--green)}
.feature-icon.blue{background:var(--blue);outline-color:var(--blue)}
.feature h3{font-family:"Raleway",sans-serif;font-weight:400;font-size:11.5px;margin-top:9px;color:#333}
.feature p{font-size:7.2px;color:#999;line-height:11.5px;margin-top:6px;white-space:nowrap}
.btn-outline{display:inline-block;margin-top:10px;border:1px solid #444;font-size:6px;padding:4px 12px;width:64px;color:#333}
/* cards */
.card{position:absolute;top:806px;width:175px;height:186px;border:1px solid var(--line);background:#fff;text-align:center}
.card-img{margin:6px 6px 0;height:90px}
.card h3{font-family:"Raleway",sans-serif;font-weight:400;font-size:12.5px;margin-top:9px;color:#333}
.card p{font-size:6.8px;color:#999;line-height:11.5px;margin:5px 6px 0;white-space:nowrap}
.btn-blue{display:inline-block;background:var(--blue);color:#fff;font-size:6px;font-weight:600;width:61px;padding:5px 0;margin-top:9px}
/* footer */
.footer{left:0;top:1023px;width:683px;height:142px;background:linear-gradient(#ececec,#f7f7f7)}
.footer .brand{left:63px;top:50px}
.fcol{position:absolute;top:30px}
.fcol h4{font-family:"Raleway",sans-serif;font-weight:500;font-size:9.5px;color:var(--blue);margin-bottom:6px}
.fcol li{list-style:none;font-size:6.6px;color:#555;line-height:16px;white-space:nowrap}
.social{display:flex;gap:4px;margin-top:6px}
.social i{width:19px;height:19px;border-radius:50%;background:var(--blue);display:block}
.bottom{left:0;top:1165px;width:683px;height:35px;background:#f0f0f0;font-size:6.6px;color:#555;padding:13px 0 0 92px}
</style>
</head>
<body>

<header>
  <div class="abs brand"><span class="brand-mark"></span><span class="brand-name">The Corvel Dental Centre</span></div>
  <div class="abs hours">Opening times<span>&#9719; OPEN 8 AM TO 8PM 7 DAYS A WEEK</span></div>
  <div class="abs call"><small>Call Us Now</small><b><svg width="10" height="10" viewBox="0 0 24 24"><path fill="#6cbf3a" d="M6.6 10.8a15 15 0 0 0 6.6 6.6l2.2-2.2c.3-.3.7-.4 1-.2 1.1.4 2.3.6 3.6.6.6 0 1 .4 1 1V20c0 .6-.4 1-1 1A17 17 0 0 1 3 4c0-.6.4-1 1-1h3.5c.6 0 1 .4 1 1 0 1.3.2 2.5.6 3.6.1.3 0 .7-.2 1z"/></svg>08 5550 2718</b></div>
</header>

<nav class="abs nav">
  <a class="active">HOME</a><a>MEET THE TEAM</a><a>DENTAL TREATMENT</a><a>DENTAL ADVICE</a><a>CONTACT US</a>
</nav>

<section class="abs hero" role="img" aria-label="Photo of smiling patients and staff in the clinic"></section>
<div class="abs hero-text"><p>WE OFFER A WALK IN SERVICE</p><h1>FOR DENTAL TREATMENTS</h1></div>
<div class="abs dots"><i class="on"></i><i></i><i></i><i></i></div>

<section class="abs welcome">
  <h2>Welcome to The Corvel Dental Centre</h2>
  <p>Your general and cosmetic dentist in the heart of vibrant Fenwick Vale. Whether it's<br>cosmetic hygiene treatment, tooth whitening, or botox facial rejuvenation.<br>Located within the busy medical centre with free parking all around.</p>
  <p class="note">Please call or pop in and one of our helpful team will be only too happy to help<br>for all your dental needs.</p>
  <div class="welcome-actions"><span class="btn-green">VIEW VIDEOS</span><span class="partner"><i></i>Medi Portal</span></div>
</section>

<div class="abs video">
  <div class="video-frame" role="img" aria-label="Video still of a treatment room with a green dental chair"></div>
  <svg class="play" width="44" height="44" viewBox="0 0 44 44"><circle cx="22" cy="22" r="20" fill="none" stroke="#fff" stroke-width="2.5"/><path d="M17 13l13 9-13 9z" fill="none" stroke="#fff" stroke-width="2.5" stroke-linejoin="round"/></svg>
  <div class="video-bar">
    <svg width="7" height="8" viewBox="0 0 7 8"><path d="M0 0l7 4-7 4z" fill="#fff"/></svg>
    <div class="track"><i></i></div>
    <svg width="10" height="8" viewBox="0 0 10 8"><path d="M0 2.5h2L5 0v8L2 5.5H0z" fill="#fff"/><path d="M6.5 2a3 3 0 0 1 0 4M8 1a5 5 0 0 1 0 6" stroke="#fff" fill="none"/></svg>
  </div>
</div>

<section class="abs features">
  <div class="feature" style="left:60px">
    <div class="feature-icon"><svg width="40" height="40" viewBox="0 0 40 40" fill="none" stroke="#fff" stroke-width="2" stroke-linecap="round"><path d="M6 34L24 16"/><circle cx="28" cy="12" r="4"/><path d="M12 36L30 18"/></svg></div>
    <h3>Dental Treatment</h3>
    <p>We provide all your general dentistry needs.<br>We also offer an emergency service</p>
    <span class="btn-outline">LEARN MORE</span>
  </div>
  <div class="feature" style="left:250px">
    <div class="feature-icon blue"><svg width="44" height="20" viewBox="0 0 44 20" fill="none" stroke="#fff" stroke-width="2.5"><path d="M3 6q19 10 38 0"/><rect x="8" y="6" width="6" height="7" rx="1"/><rect x="19" y="8" width="6" height="7" rx="1"/><rect x="30" y="6" width="6" height="7" rx="1"/></svg></div>
    <h3>Dental Advice</h3>
    <p>Free dentist advise call back- So a dentist will<br>call you back for free to discuss</p>
    <span class="btn-outline">LEARN MORE</span>
  </div>
  <div class="feature" style="left:440px">
    <div class="feature-icon"><svg width="36" height="30" viewBox="0 0 36 30" fill="#fff"><circle cx="18" cy="8" r="5"/><circle cx="7" cy="10" r="4"/><circle cx="29" cy="10" r="4"/><path d="M9 28q0-12 9-12t9 12z"/><path d="M0 26q0-10 7-10 3 0 4 2-3 3-3 8z"/><path d="M36 26q0-10-7-10-3 0-4 2 3 3 3 8z"/></svg></div>
    <h3>Meet the Team</h3>
    <p>We want our patients to feel safe, happy and<br>have dental treatment which is accessible</p>
    <span class="btn-outline">LEARN MORE</span>
  </div>
</section>

<article class="card" style="left:73px">
  <div class="card-img" role="img" aria-label="Photo of dentists treating patients at a charity clinic" style="background:linear-gradient(135deg,#c9c3bb,#6b6660 60%,#a8a29a)"></div>
  <h3>Facial Aesthetics</h3>
  <p>Botox Wrinkle reduction and Derma Fillers at<br>The Corvel Dental Centre.</p>
  <span class="btn-blue">READ MORE</span>
</article>
<article class="card" style="left:255px">
  <div class="card-img" role="img" aria-label="Close-up photo of a smile before and after whitening" style="background:linear-gradient(180deg,#d98a72,#c2503f 35%,#f1ece4 50%,#b84a3c 70%,#e0a08a)"></div>
  <h3>Teeth Whitening</h3>
  <p>Now you can whiten your smile with our<br>custom fitted whitening trays in the comfort</p>
  <span class="btn-blue">READ MORE</span>
</article>
<article class="card" style="left:437px">
  <div class="card-img" role="img" aria-label="Group photo of the dental mission team" style="background:linear-gradient(180deg,#e7e2dc 0%,#6f89a8 45%,#4c607a 75%,#8a8580)"></div>
  <h3>Our Doctors &amp; Team</h3>
  <p>Dr Arlen was the owner of a highly successful<br>Private practice in London. He has extensive</p>
  <span class="btn-blue">READ MORE</span>
</article>

<footer class="abs footer">
  <div class="abs brand"><span class="brand-mark"></span><span class="brand-name">The Corvel Dental Centre</span></div>
  <div class="fcol" style="left:246px"><h4>QUICK LINKS</h4><ul><li>Home</li><li>Who we are</li><li>What we do</li><li>Client Experiences</li></ul></div>
  <div class="fcol" style="left:354px"><h4>RESOURCES</h4><ul><li>Promotions</li><li>Career Opportunities</li><li>Contact us</li></ul><div class="social"><i></i><i></i><i></i><i></i></div></div>
  <div class="fcol" style="left:465px"><h4>CONTACT US</h4><ul><li>Unit 4, 18 Larkmoor Boulevard,</li><li>Fenwick Vale, WA 6071,</li><li>Phone: 08 5550 2718</li><li>OPEN 8 AM TO 8PM 7 DAYS A WEEK</li></ul></div>
</footer>
<div class="abs bottom">© 2016 Company Name&nbsp; All right reserved</div>

</body>
</html>
```